Brusola Card Design Project

Our company,Brusola, is focusing B to B, and people receiving this card are managers or engineers in the handset maker in the world.
Therefore we hope this to be designed strictly serious one but it needs cool and unique style which could imagine something innovation from the card.

This card will be used for Japanese,Chinese and English.
Please consider 2 byte character usage.

It Company

```html
<!DOCTYPE html>
<html lang="en">
<head>
<meta charset="utf-8">
<title>Brusola Business Card</title>
<link href="https://fonts.googleapis.com/css2?family=Questrial&display=swap" rel="stylesheet">
<style>
  :root {
    --stage: #1d1d1f;
    --card: #e9eee4;
    --card-edge: #dfe5d9;
    --ink: #1c1c1c;
    --ink-soft: #3a3a3a;
    --brand-grey: #6e6f72;
    --url-band: #8c8e90;
    --url-text: #f2f4ef;
    --accent-blue: #34509c;
    --divider: #b9bdb5;
  }
  * { margin: 0; padding: 0; box-sizing: border-box; }
  html, body {
    width: 1200px;
    height: 900px;
    overflow: hidden;
    background: var(--stage);
    font-family: "Questrial", "Century Gothic", sans-serif;
  }
  .stage {
    position: relative;
    width: 1200px;
    height: 900px;
  }
  .card {
    position: absolute;
    left: 250px;
    width: 700px;
    height: 400px;
    background: var(--card);
    border-radius: 26px;
    overflow: hidden;
  }
  .card--back { top: 40px; }
  .card--front { top: 460px; }

  /* Back side */
  .back-brand {
    position: absolute;
    top: 150px;
    left: 0;
    width: 100%;
    text-align: center;
    font-size: 64px;
    letter-spacing: 2px;
    color: var(--brand-grey);
  }
  .back-url {
    position: absolute;
    top: 262px;
    left: 50%;
    transform: translateX(-50%);
    width: 300px;
    height: 34px;
    background: var(--url-band);
    color: var(--url-text);
    font-size: 18px;
    line-height: 34px;
    text-align: center;
    letter-spacing: 0.5px;
  }

  /* Front side */
  .front-brand {
    position: absolute;
    top: 150px;
    left: 30px;
    width: 200px;
    text-align: center;
    font-size: 38px;
    letter-spacing: 1px;
    color: var(--brand-grey);
  }
  .front-divider {
    position: absolute;
    left: 248px;
    top: 70px;
    width: 1px;
    height: 210px;
    background: var(--divider);
  }
  .contact {
    position: absolute;
    left: 278px;
    top: 62px;
    color: var(--ink);
  }
  .contact-name { font-size: 30px; line-height: 32px; }
  .contact-role { font-size: 17px; color: var(--ink-soft); margin-left: 8px; line-height: 18px; }
  .contact-address {
    font-size: 19px;
    line-height: 21px;
    margin-top: 12px;
    color: var(--ink-soft);
  }
  .contact-lines { margin-top: 20px; list-style: none; }
  .contact-lines li {
    display: flex;
    align-items: center;
    font-size: 24px;
    height: 38px;
    letter-spacing: 1px;
  }
  .contact-lines svg {
    width: 22px;
    height: 22px;
    margin-right: 16px;
    flex: none;
  }
  .accent-band {
    position: absolute;
    left: 0;
    bottom: 0;
    width: 100%;
    height: 48px;
    background: var(--accent-blue);
  }
</style>
</head>
<body>
<main class="stage">

  <section class="card card--back" aria-label="Card back">
    <div class="back-brand">BRUSOLA</div>
    <div class="back-url">www.brusola.com</div>
  </section>

  <section class="card card--front" aria-label="Card front">
    <div class="front-brand">BRUSOLA</div>
    <div class="front-divider"></div>

    <div class="contact">
      <div class="contact-name">Daniel Reyes</div>
      <div class="contact-role">director</div>
      <div class="contact-address">48 Harbor Lane, Oakridge<br>CA 2041</div>
      <ul class="contact-lines">
        <li>
          <svg viewBox="0 0 24 24" aria-hidden="true">
            <path d="M6.5 3.5 L9 3 L10.5 7.5 L8.5 9 C9.5 11.5 12 14 14.5 15 L16 13 L20.5 14.5 L20 17 C19.5 19 17.5 20 15.5 19.5 C9.5 18 5.5 13.5 4.5 8 C4.2 6 5 4 6.5 3.5 Z" fill="#2a2a2a"/>
          </svg>
          415 760 3128
        </li>
        <li>
          <svg viewBox="0 0 24 24" aria-hidden="true">
            <rect x="7" y="4" width="10" height="17" rx="1.5" fill="none" stroke="#2a2a2a" stroke-width="1.8"/>
            <line x1="9" y1="1.5" x2="9" y2="4" stroke="#2a2a2a" stroke-width="1.8"/>
            <rect x="9" y="6.5" width="6" height="5" fill="#2a2a2a"/>
            <circle cx="12" cy="16.5" r="1.3" fill="#2a2a2a"/>
          </svg>
          627 509 1843
        </li>
        <li>
          <svg viewBox="0 0 24 24" aria-hidden="true">
            <rect x="2" y="5" width="20" height="14" fill="none" stroke="#2a2a2a" stroke-width="1.8"/>
            <polyline points="2,5 12,13 22,5" fill="none" stroke="#2a2a2a" stroke-width="1.8"/>
          </svg>
          support@brusola.com
        </li>
      </ul>
    </div>

    <div class="accent-band"></div>
  </section>

</main>
</body>
</html>
```